Poster Design - Stand Up Paddle Eco Tour

We need a A3 size poster design (using Adobe Illustrator) for our company's stand up paddle tour. Our tour is on flat water, calm and safe, suitable for all ages and level.

WE provide worldclass SUP boards for our customers. And branded Tovar Helsby life jacket. Our instructors are all well trained and exeprience. Plus they are super friendly. Every paddling trip come with a safety boat.

Please refer to attached files for text and photos.

Our website is www.brimwakeglide.com.sg

IMPORTANT NOTE - The design has to be done in Adobe Illustrator. The winning designer has to submit the working file in Adobe Illustrator.

Target Market(s)

Working adult - 20 - 35 year old

Industry/Entity Type

Tourism

Requirements
Must have
• The project MUST be done in Adobe Illustrator and the winning designer has to submit the artwork to us in Adobe Illustrator format.
Nice to have
• pleasant to look at.

```html
<!DOCTYPE html>
<html lang="en">
<head>
<meta charset="utf-8">
<title>Brimwake Glide – SUP Eco Tour Poster</title>
<link href="https://fonts.googleapis.com/css2?family=Roboto+Condensed:wght@300;400;700;800&display=swap" rel="stylesheet">
<style>
  :root {
    --backdrop: #e6e6e6;
    --orange: #ef7f22;
    --navy: #1c2d40;
    --white: #ffffff;
    --ink: #1c2d40;
    --muted: #2b2b2b;
    --chevron-shade: #dcdfe3;
    --sky: #b9cfe3;
    --water: #8fa7a8;
    --forest: #4c6b45;
  }
  * { box-sizing: border-box; margin: 0; padding: 0; }
  html, body { width: 849px; height: 1200px; overflow: hidden; }
  body {
    background: var(--backdrop);
    font-family: "Roboto Condensed", "Arial Narrow", sans-serif;
    position: relative;
  }
  .poster {
    position: absolute; left: 42px; top: 60px;
    width: 765px; height: 1080px;
    background: var(--white);
  }
  .headline-band {
    position: absolute; left: 0; top: 0; width: 765px; height: 150px;
    background: var(--orange);
    color: var(--white);
    text-align: center;
    padding-top: 19px;
    font-weight: 300;
    font-size: 34px;
    line-height: 39px;
  }
  .headline-band strong { font-weight: 800; }
  .photo { position: absolute; }
  .photo-hero {
    left: 0; top: 160px; width: 765px; height: 255px;
    background: linear-gradient(180deg, var(--sky) 0%, #dfe8ef 30%, #6f8a70 34%, var(--water) 40%, #9aa9a6 100%);
  }
  .photo-mangrove {
    top: 427px; width: 241px; height: 180px;
    background: linear-gradient(180deg, #cfe0ee 0%, var(--forest) 35%, #5f7456 55%, #9d9f86 100%);
  }
  .photo-mangrove.one { left: 15px; }
  .photo-mangrove.two { left: 263px; background: linear-gradient(180deg, #a9c4dd 0%, #e6edf2 40%, #6f8c71 48%, #aeb8b3 60%, #9aa8a4 100%); }
  .photo-mangrove.three { left: 513px; }
  .story-panel {
    position: absolute; left: 0; top: 620px; width: 765px; height: 260px;
  }
  .story-panel svg { position: absolute; left: 0; top: 0; }
  .story-text {
    position: absolute; left: 40px; top: 13px; width: 685px;
    color: var(--white); text-align: center;
    font-size: 21px; line-height: 25px; font-weight: 400;
  }
  .story-text p + p { margin-top: 31px; }
  .booking {
    position: absolute; left: 28px; top: 855px; width: 270px;
    color: var(--ink);
  }
  .booking h2 {
    width: 205px;
    font-size: 19px; line-height: 24px; font-weight: 800;
    text-transform: uppercase; letter-spacing: 0.3px;
  }
  .contact-list { list-style: none; margin-top: 14px; }
  .contact-list li {
    display: flex; align-items: center; gap: 12px;
    font-size: 18px; color: var(--muted); height: 30px;
  }
  .contact-list svg { flex: 0 0 20px; }
  .schedule {
    position: absolute; right: 26px; top: 854px; width: 240px;
    text-align: right; color: var(--muted);
    font-size: 18px; line-height: 24px;
  }
  .schedule h3 {
    font-size: 19px; font-weight: 800; color: var(--ink);
    letter-spacing: 0.3px; line-height: 24px;
  }
  .schedule p { margin-bottom: 2px; }
  .footer-band {
    position: absolute; left: 0; bottom: 0; width: 765px; height: 40px;
    background: var(--orange);
  }
  .brand-badge {
    position: absolute; left: 307px; top: 900px; width: 150px; height: 172px;
  }
  .brand-badge svg { position: absolute; left: 0; top: 0; }
  .brand-name {
    position: absolute; left: 0; top: 72px; width: 150px;
    text-align: center; color: var(--navy);
    font-size: 21px; line-height: 24px; font-weight: 700;
  }
</style>
</head>
<body>
  <main class="poster">
    <header class="headline-band">
      EXPLORE THE <strong>NATURAL COASTAL</strong> SURROUNDINGS<br>
      AND <strong>WATERWAYS OF JOHOR</strong> ON A <strong>SUP ADVENTURE</strong><br>
      <strong>TOURING BOARD</strong>
    </header>

    <div class="photo photo-hero" role="img" aria-label="Group photo of paddlers on stand up paddle boards in life vests on calm coastal water, with a safety boat and fish farm huts behind"></div>
    <div class="photo photo-mangrove one" role="img" aria-label="Paddlers heading along a mangrove-lined river"></div>
    <div class="photo photo-mangrove two" role="img" aria-label="Paddlers spread out on open flat water under a blue sky"></div>
    <div class="photo photo-mangrove three" role="img" aria-label="Two paddlers standing on yellow boards near the mangroves"></div>

    <section class="story-panel">
      <svg width="765" height="260" viewBox="0 0 765 260">
        <polygon points="0,180 382,262 765,180 765,200 382,262 0,200" fill="var(--chevron-shade)"/>
        <polygon points="0,0 765,0 765,180 382,260 0,180" fill="var(--navy)"/>
      </svg>
      <div class="story-text">
        <p>Our tours are flat-water and appropriate for all ages and levels. We have the best possible service and equipment. Join us for a fun and relaxing day.</p>
        <p>What could be better than a group guided tour? With life vests and a safety boat for our guided tour, you can be assured of a secured environment while you focus on just having fun and creating life’s best memories with friends and family.</p>
      </div>
    </section>

    <section class="booking">
      <h2>Contact us for booking. We do not accept walk-in.</h2>
      <ul class="contact-list">
        <li>
          <svg width="20" height="20" viewBox="0 0 20 20" fill="none" stroke="var(--orange)" stroke-width="1.6">
            <circle cx="10" cy="10" r="8.2"/><ellipse cx="10" cy="10" rx="3.6" ry="8.2"/>
            <line x1="2" y1="10" x2="18" y2="10"/><line x1="3.5" y1="5.5" x2="16.5" y2="5.5"/><line x1="3.5" y1="14.5" x2="16.5" y2="14.5"/>
          </svg>
          www.brimwakeglide.com.sg
        </li>
        <li>
          <svg width="20" height="20" viewBox="0 0 20 20"><circle cx="10" cy="10" r="6" fill="var(--orange)"/></svg>
          Brimwake Glide
        </li>
        <li>
          <svg width="20" height="20" viewBox="0 0 20 20" fill="none" stroke="var(--orange)" stroke-width="1.6">
            <rect x="1.5" y="4" width="17" height="12"/><polyline points="1.5,4 10,11 18.5,4"/>
          </svg>
          booking@brimwakeglide.com.sg
        </li>
      </ul>
    </section>

    <section class="schedule">
      <h3>TIMING:</h3>
      <p>Morning, Afternoon, and<br>Sunset Session</p>
      <h3>LOCATION:</h3>
      <p>Selwyn River, set off from<br>Harrow Point, Marlow Bay.<br>(next to Fenwick Cove)</p>
    </section>

    <div class="footer-band"></div>

    <div class="brand-badge">
      <svg width="150" height="172" viewBox="0 0 150 172">
        <path d="M75 4 C120 4 150 30 150 80 C150 135 115 172 75 172 C35 172 0 135 0 80 C0 30 30 4 75 4 Z" fill="var(--white)"/>
      </svg>
      <div class="brand-name">Brimwake<br>Glide</div>
    </div>
  </main>
</body>
</html>
```